Looking for updated Letterhead and Compliments Slips to go with our new updated logo. This stationary will be used for letters to suppliers and customers so needs to be practical while also quite classic.

We are an engineering company so needs to be clean and precise

Target Market(s)

SME'S and large automotive customers

Industry/Entity Type

Automotive

Font styles to use
Sans Serif

Colors
85acd3
0356a4
0792cd
33a6d7
85abd2
ffffff

Requirements
Must have
• Address details as below
• KT Fabrications Limited
• Hallmere Road
• Brackwell
• Oakshire
• LP47 9XZ, UK
• Telephone: +44 (0)1632 960418
• Fax: +44 (0)1632 960733
• Email: sales@ktfabrications.example
• Web: www.ktfabrications.example
Nice to have
• Nice to have some element of being a British Manufacturer

```html
<!DOCTYPE html>
<html lang="en">
<head>
<meta charset="utf-8">
<title>KT Fabrications Stationery</title>
<link rel="stylesheet" href="https://fonts.googleapis.com/css2?family=Source+Sans+3:wght@400;600&family=Great+Vibes&display=swap">
<style>
  :root {
    --backdrop: #a9a8a9;
    --paper: #f5f4f2;
    --ink: #1f1f1f;
    --body-ink: #555555;
    --brand-blue: #0356a4;
    --light-blue: #85acd3;
    --band-black: #0d0d0d;
    --white: #ffffff;
  }
  * { margin: 0; padding: 0; box-sizing: border-box; }
  html, body { width: 1200px; height: 770px; overflow: hidden; }
  body {
    background: var(--backdrop);
    font-family: "Source Sans 3", sans-serif;
    color: var(--ink);
    position: relative;
  }
  .sheet {
    position: absolute;
    background: var(--paper);
    box-shadow: 1px 2px 4px rgba(0,0,0,0.35);
    overflow: hidden;
  }
  .letterhead { left: 62px; top: 33px; width: 496px; height: 701px; }
  .comp-slip { left: 583px; top: 477px; width: 561px; height: 253px; }

  .brand {
    position: absolute;
    display: flex;
    align-items: center;
    gap: 7px;
    font-family: "Source Sans 3", sans-serif;
    font-weight: 400;
    font-size: 12px;
    letter-spacing: 3.6px;
    color: var(--brand-blue);
    white-space: nowrap;
  }
  .brand-dot {
    width: 9px; height: 9px;
    border-radius: 50%;
    background: var(--brand-blue);
  }
  .letterhead .brand { left: 35px; top: 93px; }
  .comp-slip .brand { left: 23px; top: 61px; }

  .contact-block {
    position: absolute;
    left: 336px; top: 46px;
    font-size: 8px;
    line-height: 10.5px;
    color: var(--ink);
    font-style: normal;
  }
  .contact-block .line { display: flex; align-items: center; gap: 4px; margin-top: 1.5px; }
  .icon { width: 8px; height: 7px; fill: var(--brand-blue); flex: none; }

  .salutation {
    position: absolute;
    left: 35px; top: 197px;
    font-size: 13px;
    color: #444;
  }
  .letter-body {
    position: absolute;
    left: 35px; top: 236px;
    width: 426px;
    font-size: 7.9px;
    line-height: 12px;
    color: var(--body-ink);
    text-align: justify;
  }
  .letter-body p { margin-bottom: 12px; }
  .sign-off {
    position: absolute;
    left: 35px; top: 489px;
    font-size: 7.9px;
    color: var(--body-ink);
  }
  .signature-mark {
    position: absolute;
    left: 50px; top: 508px;
    width: 62px; height: 20px;
    background: linear-gradient(90deg, rgba(30,30,30,0.15), rgba(30,30,30,0.05));
    border-radius: 3px;
  }
  .signatory {
    position: absolute;
    left: 53px; top: 542px;
    font-size: 8.5px;
    line-height: 13px;
    color: var(--body-ink);
  }

  .footer-band {
    position: absolute;
    left: 0; bottom: 0;
    width: 100%;
  }
  .letterhead .footer-band { height: 20px; }
  .comp-slip .footer-band { height: 16px; }
  .footer-band svg { display: block; width: 100%; height: 100%; }
  .web-address {
    position: absolute;
    right: 36px; bottom: 5px;
    font-size: 7.5px;
    letter-spacing: 2.2px;
    color: var(--white);
  }

  .slip-address {
    position: absolute;
    left: 24px; top: 200px;
    font-size: 8px;
    color: var(--ink);
    white-space: nowrap;
  }
  .slip-rule {
    position: absolute;
    left: 24px; top: 212px;
    width: 497px; height: 0;
    border-top: 0.6px solid #888;
  }
  .slip-contacts {
    position: absolute;
    left: 24px; top: 216px;
    display: flex; align-items: center; gap: 3px;
    font-size: 8px;
    color: var(--ink);
    white-space: nowrap;
  }
  .slip-contacts span { margin-right: 2px; }
  .compliments {
    position: absolute;
    left: 292px; top: 164px;
    font-family: "Great Vibes", cursive;
    font-size: 37px;
    color: var(--brand-blue);
    white-space: nowrap;
  }
</style>
</head>
<body>

<svg width="0" height="0" style="position:absolute" aria-hidden="true">
  <defs>
    <symbol id="icon-phone" viewBox="0 0 10 10"><path d="M2 0.5l2 2-1 1.2c.6 1.3 1.6 2.3 2.9 2.9l1.2-1 2 2-1.3 1.9C4.5 9.3.7 5.5.5 1.6z"/></symbol>
    <symbol id="icon-fax" viewBox="0 0 10 9"><rect x="2.5" y="0" width="5" height="2.5"/><rect x="0" y="3" width="10" height="4"/><rect x="2.5" y="6" width="5" height="3" fill="#f5f4f2" stroke="#0356a4" stroke-width="0.8"/></symbol>
    <symbol id="icon-mail" viewBox="0 0 10 7"><rect x="0" y="0" width="10" height="7"/><path d="M0.5 0.5L5 4l4.5-3.5" fill="none" stroke="#f5f4f2" stroke-width="0.9"/></symbol>
  </defs>
</svg>

<section class="sheet letterhead" aria-label="Letterhead">
  <div class="brand"><span class="brand-dot"></span>KT FABRICATIONS</div>

  <address class="contact-block">
    <div>KT Fabrications Limited</div>
    <div>Hallmere Road, Brackwell, Oakshire</div>
    <div class="line" style="margin-top:5px"><svg class="icon"><use href="#icon-phone"/></svg>+44 (0)1632 960418</div>
    <div class="line"><svg class="icon"><use href="#icon-fax"/></svg>+44 (0)1632 960733</div>
    <div class="line"><svg class="icon"><use href="#icon-mail"/></svg>sales@ktfabrications.example</div>
  </address>

  <div class="salutation">Dear Mr. Harlow,</div>

  <div class="letter-body">
    <p>Lorem ipsum dolor sit amet, consectetur adipiscing elit. Donec orci purus, luctus vitae dignissim eu, iaculis sed purus. Vivamus faucibus, ipsum nec aliquet viverra, leo mauris condimentum ligula, sit amet sagittis enim ligula quis arcu. Nam egestas tortor id nisi porttitor mattis. In tortor ante, ultricies in suscipit a, tempus non massa. Vivamus et auctor mi. Fusce vel massa nulla. Phasellus nec eros mauris, et scelerisque orci.</p>
    <p>Donec malesuada orci vitae nulla accumsan porta a id massa. Quisque accumsan iaculis magna sit amet fringilla. Maecenas consequat, magna eget tincidunt semper, odio nibh rutrum mi, id feugiat ante nisi eu risus. Vestibulum nunc orci, rhoncus a placerat in, ultricies in mi. Cras mattis varius eros, vel fringilla nisi suscipit eget. Quisque scelerisque sagittis nulla at porttitor.</p>
    <p>Sed id augue vitae urna euismod commodo aliquet a quam. Pellentesque arcu velit, cursus et malesuada ut, consequat et diam. Nullam erat sem, rhoncus id ullamcorper vitae, rhoncus et arcu. In ultricies ultricies nulla, ut rutrum nisi iaculis at. Donec eu magna a metus ornare faucibus. Fusce aliquet faucibus ultricies. Morbi semper, est id tincidunt gravida, sem arcu adipiscing lacus, ac bibendum nulla leo eu purus. Quisque nec diam sed risus consectetur a ccumsan quis quis nibh. Vestibulum id purus lorem.</p>
    <p>It is a long established fact that a reader will be distracted by the readable content of a page when looking at its layout. The point of using Lorem Ipsum is that it has a more-or-less normal distribution of letters, as opposed to using 'Content here, content here', making it look like readable English. Many desktop publishing packages</p>
  </div>

  <div class="sign-off">Sincerely,</div>
  <div class="signature-mark" role="img" aria-label="Handwritten signature"></div>
  <div class="signatory">Daniel Harlow<br>CEO/ Founder</div>

  <div class="footer-band">
    <svg viewBox="0 0 496 20" preserveAspectRatio="none" aria-hidden="true">
      <polygon points="0,2 296,2 291,20 0,20" fill="var(--brand-blue)"/>
      <rect x="0" y="7.5" width="296" height="1.6" fill="var(--white)"/>
      <rect x="0" y="13.5" width="296" height="1.6" fill="var(--white)"/>
      <polygon points="298,0 496,0 496,20 292,20" fill="var(--band-black)"/>
    </svg>
    <div class="web-address">www.ktfabrications.example</div>
  </div>
</section>

<section class="sheet comp-slip" aria-label="Compliments slip">
  <div class="brand"><span class="brand-dot"></span>KT FABRICATIONS</div>

  <div class="compliments">With Compliments</div>
  <div class="slip-address">KT Fabrications Limited Hallmere Road, Brackwell, Oakshire</div>
  <div class="slip-rule"></div>
  <div class="slip-contacts">
    <svg class="icon"><use href="#icon-phone"/></svg><span>+44 (0)1632 960418</span>
    <svg class="icon"><use href="#icon-fax"/></svg><span>+44 (0)1632 960733</span>
    <svg class="icon"><use href="#icon-mail"/></svg><span>sales@ktfabrications.example</span>
  </div>

  <div class="footer-band">
    <svg viewBox="0 0 561 16" preserveAspectRatio="none" aria-hidden="true">
      <polygon points="0,2 360,2 356,16 0,16" fill="var(--brand-blue)"/>
      <rect x="0" y="6.5" width="360" height="1.3" fill="var(--white)"/>
      <rect x="0" y="11" width="360" height="1.3" fill="var(--white)"/>
      <polygon points="362,0 561,0 561,16 357,16" fill="var(--band-black)"/>
    </svg>
  </div>
</section>

</body>
</html>
```